skin elixir serum with snail extract

I am working at a natural skincare company. We are going to launch a new product - a skin serum. completely natural, super concentrated, multi use (face, neck , eyes). But we need the packaging (box and bottle label) to be aligned to our brand's philosophy, design etc. (See more at pindomare.com)

Here's a more detailed description :
"Elevate your skincare routine with Brusquel Elixir, the ultimate one-drop wonder enriched with potent snail secretion. Experience the magic as our 100% natural serum transforms your face, eyes, décolleté, and neck. Get ready to say Wow to a new level of radiance!"

Target Market(s)

natural skincare enthusiasts - beauty pioneers

Industry/Entity Type

beauty - wellness

Requirements
Nice to have
• based on the overall brand philosophy (see pindomare.com)

```html
<!DOCTYPE html>
<html lang="en">
<head>
<meta charset="utf-8">
<title>Pindomare Skin Serum Packaging</title>
<link href="https://fonts.googleapis.com/css2?family=Montserrat:wght@300;400&display=swap" rel="stylesheet">
<style>
  :root {
    --page: #ffffff;
    --cream: #e9e6d4;
    --cream-light: #efece0;
    --sage: #7b8672;
    --sage-ornament: #8f9a84;
    --ink: #3b3b3b;
    --ink-soft: #8a8a80;
    --cream-text: #ece8d6;
  }
  html, body {
    margin: 0;
    width: 1200px;
    height: 1200px;
    overflow: hidden;
    background: var(--page);
    font-family: "Montserrat", sans-serif;
  }
  .canvas { position: relative; width: 1200px; height: 1200px; }

  /* Box */
  .box-side {
    position: absolute; left: 470px; top: 140px; width: 160px; height: 990px;
    background: var(--cream);
  }
  .box-side .ornament {
    position: absolute; left: 20px; top: 30px; width: 120px; height: 930px;
    background: linear-gradient(180deg, var(--sage-ornament), #a9b19c 50%, var(--sage-ornament));
    opacity: .55; border-radius: 60px;
  }
  .box-front {
    position: absolute; left: 630px; top: 135px; width: 310px; height: 995px;
    background: var(--sage);
    border-right: 14px solid var(--cream);
    color: var(--cream-text);
    text-align: center;
    box-sizing: border-box;
  }
  .box-front .brand { position: absolute; top: 115px; left: 0; right: 0; font-size: 40px; font-weight: 300; letter-spacing: 1px; }
  .box-front .tagline { position: absolute; top: 200px; left: 0; right: 0; font-size: 13px; letter-spacing: 3px; }
  .box-front .kicker { position: absolute; top: 575px; left: 0; right: 0; font-size: 19px; line-height: 1.4; font-weight: 400; }
  .box-front .product { position: absolute; top: 650px; left: 0; right: 0; font-size: 40px; font-weight: 400; letter-spacing: 1px; }
  .box-front .uses { position: absolute; top: 735px; left: 0; right: 0; font-size: 19px; }
  .box-front .ornament {
    position: absolute; top: 840px; left: 45px; width: 225px; height: 90px;
    background: linear-gradient(180deg, #b9bca8, #9aa28e); border-radius: 45px; opacity: .8;
  }

  /* Bottle label */
  .bottle-label {
    position: absolute; left: 270px; top: 470px; width: 235px; height: 625px;
    background: var(--cream-light);
    border-radius: 0 0 14px 14px;
    color: var(--ink);
    text-align: center;
    box-shadow: 0 0 0 1px #dedbc8;
  }
  .bottle-label .brand { position: absolute; top: 55px; left: 0; right: 0; font-size: 32px; font-weight: 300; }
  .bottle-label .tagline { position: absolute; top: 118px; left: 0; right: 0; font-size: 9px; letter-spacing: 2px; color: var(--ink-soft); }
  .bottle-label .kicker { position: absolute; top: 175px; left: 0; right: 0; font-size: 18px; line-height: 1.45; }
  .bottle-label .product { position: absolute; top: 300px; left: 0; right: 0; font-size: 44px; line-height: 1.25; font-weight: 400; }
  .bottle-label .uses { position: absolute; top: 448px; left: 0; right: 0; font-size: 19px; }
  .bottle-label .ornament {
    position: absolute; top: 525px; left: 30px; width: 175px; height: 70px;
    background: linear-gradient(180deg, #a9b19c, #8f9a84); border-radius: 35px; opacity: .7;
  }
</style>
</head>
<body>
<div class="canvas">
  <div class="box-side">
    <div class="ornament" role="img" aria-label="Decorative floral pattern in sage green"></div>
  </div>
  <div class="box-front">
    <div class="brand">Pindomare</div>
    <div class="tagline">YOUR NATURAL LIFE</div>
    <div class="kicker">SUPER CONCENTRATED<br>NATURAL</div>
    <div class="product">SKIN SERUM</div>
    <div class="uses">face | neck | eyes</div>
    <div class="ornament" role="img" aria-label="Small cream floral ornament"></div>
  </div>
  <div class="bottle-label">
    <div class="brand">Pindomare</div>
    <div class="tagline">YOUR NATURAL LIFE</div>
    <div class="kicker">SUPER<br>CONCENTRATED<br>NATURAL</div>
    <div class="product">SKIN<br>SERUM</div>
    <div class="uses">face | neck | eyes</div>
    <div class="ornament" role="img" aria-label="Small sage floral ornament"></div>
  </div>
</div>
</body>
</html>
```